Engineering group involved with fire safety needs a business card

We need a business card design for a company based in Greece called "Varotis Group". We are engineers and specialized technicians, operating the following : a) Fire fighting equipment trade b) Installation , Inspection & Maintenance of fire extinguishers and fire protection systems c) Occupational Health & Safety (Risk assessment & management/ Staff training). We need a clear and simple card design. I uploaded a draft I made, in order to give you an idea of the company and how I currently imagine the design of the card. I also uploaded the logo in .png file format. We are always open to different, new suggestions and ideas you may want to submit.
Target Market(s)
industries, companies, managers, retail clients
Industry/Entity Type
Fire Safety
Contact Information for Business Card
Addresses & phone numbers (headquarters + branch), logo, name (you can find all the details on the uploaded files!)
Colors
Designer to choose colors to be used in the design.
Look and feel
Each slider illustrates characteristics of the customer's brand and the style your logo design should communicate.

```html
<!DOCTYPE html>
<html lang="en">
<head>
<meta charset="utf-8">
<title>Varotis Group – Business Card</title>
<link rel="stylesheet" href="https://fonts.googleapis.com/css2?family=Lato:wght@400;700&display=swap">
<style>
  :root {
    --backdrop: #d9cdb8;
    --card-light: #ffffff;
    --card-dark: #231f20;
    --brand-red: #b01e23;
    --text-grey: #55585a;
    --text-white: #ffffff;
  }
  * { margin: 0; padding: 0; box-sizing: border-box; }
  html, body { width: 1000px; height: 1200px; overflow: hidden; }
  body {
    background: var(--backdrop);
    font-family: "Lato", sans-serif;
    position: relative;
  }
  .card-side {
    position: absolute;
    top: 202px;
    width: 455px;
    height: 798px;
  }
  .card-front { left: 46px; background: var(--card-light); }
  .card-back { left: 500px; width: 456px; background: var(--card-dark); }

  .brand {
    position: absolute;
    left: 0; right: 0;
    top: 50px;
    text-align: center;
    font-weight: 700;
    line-height: 1;
  }
  .brand-mark {
    display: block;
    width: 70px; height: 70px;
    margin: 0 auto 38px;
  }
  .brand-name { display: block; font-size: 60px; letter-spacing: 2px; }
  .brand-sub { display: block; font-size: 34px; letter-spacing: 6px; margin-top: 10px; }
  .card-front .brand { color: var(--brand-red); }
  .card-front .brand-mark { background: var(--brand-red); }
  .card-back .brand { color: var(--text-white); }
  .card-back .brand-mark { background: var(--text-white); }

  .contact {
    position: absolute;
    left: 0; right: 0;
    text-align: center;
    color: var(--text-grey);
    font-size: 19px;
    line-height: 29px;
  }
  .person { top: 316px; }
  .person-name {
    color: var(--brand-red);
    font-weight: 700;
    font-size: 23px;
    letter-spacing: 0.5px;
  }
  .person-role { font-size: 18.5px; }
  .direct { top: 416px; }
  .office-hq { top: 510px; }
  .office-branch { top: 629px; }
  .office-label { color: var(--brand-red); font-weight: 700; }
  .icon { display: inline-block; vertical-align: -3px; margin-right: 5px; fill: var(--brand-red); }

  .tagline-band {
    position: absolute;
    left: 0; right: 0; bottom: 0;
    height: 50px;
    background: var(--brand-red);
    color: var(--text-white);
    font-size: 19px;
    text-align: center;
    line-height: 46px;
  }

  .services {
    position: absolute;
    left: 28px; right: 30px;
    top: 368px;
    list-style: none;
    text-align: center;
    color: var(--text-white);
    font-size: 19.5px;
    letter-spacing: 0.3px;
  }
  .services li {
    height: 47.5px;
    line-height: 36px;
    border-bottom: 1.5px solid var(--brand-red);
    padding-top: 1px;
  }
  .services li:last-child { border-bottom: none; }

  .web-contact {
    position: absolute;
    left: 0; right: 0;
    top: 646px;
    text-align: center;
    color: var(--text-white);
    font-size: 20px;
    line-height: 32px;
  }
</style>
</head>
<body>
  <section class="card-side card-front">
    <div class="brand">
      <span class="brand-mark"></span>
      <span class="brand-name">VAROTIS</span>
      <span class="brand-sub">GROUP</span>
    </div>

    <div class="contact person">
      <p class="person-name">NIKOLAOS VAROTIS</p>
      <p class="person-role">Mechanical Engineer - OHS Consultant</p>
    </div>

    <div class="contact direct">
      <p><svg class="icon" width="14" height="20" viewBox="0 0 14 20"><path d="M2 0h10a2 2 0 0 1 2 2v16a2 2 0 0 1-2 2H2a2 2 0 0 1-2-2V2a2 2 0 0 1 2-2zm0 2v14h10V2zm5 15a1 1 0 1 0 0 2 1 1 0 0 0 0-2z"/></svg>+30 690 412 58 30</p>
      <p><svg class="icon" width="17" height="12" viewBox="0 0 17 12"><path d="M0 0h17v1.5L8.5 7 0 1.5zm0 3.3 8.5 5.4L17 3.3V12H0z"/></svg>nikolaos.varotis@varotisgroup.gr</p>
    </div>

    <div class="contact office-hq">
      <p class="office-label">Headquarters:</p>
      <p>12 Agiou Georgiou, 19500 Lavrio</p>
      <p><svg class="icon" width="17" height="17" viewBox="0 0 24 24"><path d="M6.6 10.8a15.1 15.1 0 0 0 6.6 6.6l2.2-2.2a1 1 0 0 1 1-.25 11.4 11.4 0 0 0 3.6.6 1 1 0 0 1 1 1V20a1 1 0 0 1-1 1A17 17 0 0 1 3 4a1 1 0 0 1 1-1h3.5a1 1 0 0 1 1 1c0 1.25.2 2.45.6 3.6a1 1 0 0 1-.25 1z"/></svg>+30 22920 41583</p>
    </div>

    <div class="contact office-branch">
      <p class="office-label">Branch Office:</p>
      <p>22 Anthemion Street, 15124 Marousi</p>
      <p><svg class="icon" width="17" height="17" viewBox="0 0 24 24"><path d="M6.6 10.8a15.1 15.1 0 0 0 6.6 6.6l2.2-2.2a1 1 0 0 1 1-.25 11.4 11.4 0 0 0 3.6.6 1 1 0 0 1 1 1V20a1 1 0 0 1-1 1A17 17 0 0 1 3 4a1 1 0 0 1 1-1h3.5a1 1 0 0 1 1 1c0 1.25.2 2.45.6 3.6a1 1 0 0 1-.25 1z"/></svg>+30 210 5550142</p>
    </div>

    <div class="tagline-band">installation - inspection - maintenance</div>
  </section>

  <section class="card-side card-back">
    <div class="brand">
      <span class="brand-mark"></span>
      <span class="brand-name">VAROTIS</span>
      <span class="brand-sub">GROUP</span>
    </div>

    <ul class="services">
      <li>FIRE FIGHTING EQUIPMENT</li>
      <li>LICENSING &amp; BUSINESS REGISTRATION</li>
      <li>OCCUPATIONAL HEALTH &amp; SAFETY</li>
      <li>STAFF TRAINING</li>
    </ul>

    <div class="web-contact">
      <p>info@varotisgroup.gr</p>
      <p>www.varotisgroup.gr</p>
    </div>

    <div class="tagline-band">installation - inspection - maintenance</div>
  </section>
</body>
</html>
```